Business Card Design

We would like a colorful, engaging, welcoming business card, utilizing our picture of a local lighthouse. We are a Church. We would like the design to mostly feature the colour blue.
Updates
Project Deadline Extended
Reason: Because of some suggested changes that have been sent out
Thank you so much to all Designers who sent in submissions to us - it was really hard to make a decision, they were all of such high quality. We would not hesitate to recommend Sketch Harbor to other churches/ businesses.
Kestrel Beacon Fellowship
Industry/Entity Type
Business
Contact Information for Business Card
Kestrel Beacon Fellowship Inc, 17 Marrick Rd, TOVERDALE WA 6391, Ph: (08) 9517 4063, E: beaconfellowship@quorvamail.example, Friendloop logo - Kestrel Beacon Fellowship Inc, Sunday Service 10am, "For God sent not his Son into the world to condemn the world; but that the world through Him might be saved." John 3:17.
Look and feel
Each slider illustrates characteristics of the customer's brand and the style your logo design should communicate.

```html
<!DOCTYPE html>
<html lang="en">
<head>
<meta charset="utf-8">
<title>Kestrel Beacon Fellowship – Business Card</title>
<link href="https://fonts.googleapis.com/css2?family=Mukta:wght@200;500;800&display=swap" rel="stylesheet">
<style>
  :root {
    --backdrop: #b9c3c4;
    --card-white: #ffffff;
    --sky-blue: #3aa0e0;
    --deep-blue: #2f4f9a;
    --pale-blue: #8cc6ec;
    --wash-blue: #a6d1ef;
    --halo-blue: #2e8fd6;
    --text-blue: #2d4e92;
  }
  * { margin: 0; padding: 0; box-sizing: border-box; }
  html, body {
    width: 1200px; height: 1000px; overflow: hidden;
    background: var(--backdrop);
    font-family: "Mukta", "Helvetica Neue", Arial, sans-serif;
  }
  .business-card {
    position: absolute; left: 100px; top: 195px;
    width: 1000px; height: 610px; overflow: hidden;
    background:
      linear-gradient(160deg, var(--card-white) 38%, #e3f0fa 62%, var(--wash-blue) 100%);
    box-shadow: 0 18px 40px rgba(40, 55, 60, 0.28);
  }
  .lighthouse-halo {
    position: absolute; left: 420px; top: -260px;
    width: 760px; height: 760px; border-radius: 50%;
    background: radial-gradient(circle, var(--halo-blue) 0%, var(--halo-blue) 48%, #5fb0e6 56%, rgba(166,209,239,0.6) 64%, rgba(255,255,255,0) 71%);
  }
  .lighthouse-photo {
    position: absolute; left: 540px; top: -140px;
    width: 520px; height: 520px; border-radius: 50%;
    background:
      linear-gradient(168deg, #1f4fa8 0%, #3a78c8 40%, #4d7f9a 55%, #7a7a55 66%, #6c8a64 80%, #5a86a4 100%);
  }
  .brand-name {
    position: absolute; left: 78px; top: 60px;
    line-height: 0.86;
  }
  .brand-name .line-one { display: block; font-size: 70px; font-weight: 800; color: var(--sky-blue); letter-spacing: -1px; }
  .brand-name .line-two { display: block; font-size: 82px; font-weight: 800; color: var(--deep-blue); letter-spacing: -1.5px; }
  .brand-name .line-three { display: block; font-size: 58px; font-weight: 200; color: var(--pale-blue); margin-top: 8px; }
  .contact-details {
    position: absolute; left: 80px; top: 335px;
    list-style: none; color: var(--text-blue);
    font-size: 31px; font-weight: 500; line-height: 1.3;
  }
  .contact-details .phone-icon { width: 24px; height: 24px; vertical-align: -3px; margin-right: 4px; }
  .social-link {
    position: absolute; left: 560px; top: 478px;
    display: flex; align-items: center; gap: 14px;
  }
  .social-link .social-square { width: 62px; height: 62px; background: var(--deep-blue); }
  .social-link .social-text {
    color: var(--deep-blue); font-weight: 800; font-size: 26px; line-height: 1.05;
  }
  .social-link .social-text span { display: block; font-size: 38px; }
</style>
</head>
<body>
  <div class="business-card">
    <div class="lighthouse-halo"></div>
    <div class="lighthouse-photo" role="img" aria-label="Photo of a local lighthouse on a heath-covered headland under a blue sky with a bright star of light"></div>

    <h1 class="brand-name">
      <span class="line-one">Kestrel</span>
      <span class="line-two">Beacon</span>
      <span class="line-three">Fellowship Inc.</span>
    </h1>

    <ul class="contact-details">
      <li>17 Marrick Rd, TOVERDALE WA 6391</li>
      <li><svg class="phone-icon" viewBox="0 0 24 24" aria-hidden="true"><circle cx="12" cy="12" r="11" fill="none" stroke="currentColor" stroke-width="1.6"/><path d="M8 6.5c.6-.5 1.4-.4 1.8.2l1 1.6c.3.5.2 1.1-.2 1.5l-.7.6c.6 1.4 1.6 2.5 3 3.1l.6-.7c.4-.4 1-.5 1.5-.2l1.6 1c.6.4.7 1.2.2 1.8-1 1.2-2.6 1.4-4 .7-2.6-1.3-4.5-3.2-5.6-5.8-.5-1.3-.3-2.8.8-3.8z" fill="currentColor"/></svg>(08) 9517 4063</li>
      <li>e:beaconfellowship@quorvamail.example</li>
    </ul>

    <div class="social-link">
      <div class="social-square"></div>
      <p class="social-text">Find us on<span>Friendloop</span></p>
    </div>
  </div>
</body>
</html>
```